Home Page for Prospix

We need to design a new home page for Prospix.com, a provider of B2B data for sales and marketing professionals.

The home page should follow the lead of our newly re-designed header and logo (still being tweaked) and use our new color scheme. Please refer to attached file. Please use this file as as the basis of the design for the rest or the home page. No part of the header or logo needs to be altered in this project.

All submissions should be clear, fresh, clean and simple in style. We like the look and feel of tallyvine.com, costharbor.com and pollquarry.com. Please use them as references.

The main functions of the home page will be to tell the user about 1) the benefits and uses of Prospix and 2) to get them to sign up.

Based upon the successful redesign of our homepage, we will also be redesigning our subscription page and our about us page in the coming weeks.

Target Market(s)

Sales and marketing professionals. Mostly 25 - 45 year old males.

Industry/Entity Type

Marketing

Requirements
Must have
• Items needed:

1A) There should be three main points highlighted 1) Fresh Data 2) Sales Intelligence 3) Increased Bottomline. There will be further text under these headers tbd. For style/feel reference the same device used by pollquarry uses on its homepage.

1B) When you rollover these three items they should highlight and be clickable. The click will lead you to a header and paragraph about each that is further down the homepage (text tbd).

2) We also need a free trial and a sign up button. This button should move with you as you scroll up and down the homepage. Reference www.tallyvine.com.

3) We need a “Featured In” section. Also reference tallyvine.com. You can pull the content from prospix.com’s current home page.

4) We also need a social media buttons section (chatterlane, quipstream, orbitly+ and workNest)

```html
<!DOCTYPE html>
<html lang="en">
<head>
<meta charset="utf-8">
<title>Prospix — Create Surveys. Get Answers.</title>
<link rel="stylesheet" href="https://fonts.googleapis.com/css2?family=Open+Sans:wght@400;600;700&display=swap">
<style>
  :root {
    --navy: #1b3448;
    --blue: #0ea3e3;
    --blue-dark: #1a77a6;
    --blue-text: #1a9ad6;
    --green: #8cb31b;
    --green-dark: #6f9312;
    --green-text: #88b31a;
    --ink: #1a1a1a;
    --grey-text: #9a9a9a;
    --panel: #ececec;
    --card-border: #dcdcdc;
    --footer: #2b2b2b;
    --footer-line: #3d3d3d;
    --white: #ffffff;
  }
  * { box-sizing: border-box; margin: 0; padding: 0; }
  html, body { width: 1200px; height: 969px; overflow: hidden; }
  body { font-family: "Open Sans", Arial, sans-serif; color: var(--ink); background: var(--white); position: relative; }
  a { color: inherit; text-decoration: none; }

  .top-strip { position: absolute; top: 0; left: 0; width: 1200px; height: 7px; background: var(--navy); }

  .site-header { position: absolute; top: 0; left: 0; width: 1200px; height: 93px;
    background: linear-gradient(#ffffff, #f3f3f3); }
  .brand { position: absolute; left: 171px; top: 28px; display: flex; align-items: center; gap: 10px; }
  .brand-dot { width: 34px; height: 34px; border-radius: 50%; background: var(--blue); }
  .brand-name { font-size: 36px; font-weight: 700; color: var(--blue); letter-spacing: -0.5px; }

  .utility-tabs { position: absolute; top: 0; left: 868px; display: flex; gap: 6px; }
  .utility-tab { height: 24px; padding: 0 12px; background: var(--navy); color: var(--white);
    font-size: 11px; display: flex; align-items: center; gap: 6px; border-radius: 0 0 3px 3px; }
  .utility-tab svg { width: 11px; height: 11px; fill: var(--white); }
  .contact-email { position: absolute; top: 32px; right: 170px; font-size: 11px; color: var(--grey-text);
    display: flex; align-items: center; gap: 5px; }
  .social-top { position: absolute; top: 52px; right: 170px; display: flex; gap: 4px; }
  .social-chip { height: 22px; padding: 0 6px; background: var(--blue-dark); color: var(--white);
    font-size: 10px; display: flex; align-items: center; border-radius: 2px; }

  .main-nav { position: absolute; top: 93px; left: 0; width: 1200px; height: 37px; background: var(--blue); }
  .nav-list { position: absolute; left: 168px; top: 0; display: flex; list-style: none; height: 37px; }
  .nav-list li a { display: flex; align-items: center; height: 37px; padding: 0 15px;
    color: var(--white); font-size: 16px; font-weight: 600; }
  .nav-list li.is-active a { background: var(--blue-dark); border-top: 3px solid var(--navy); }
  .search-box { position: absolute; left: 837px; top: 6px; width: 193px; height: 25px; background: var(--white);
    border-radius: 2px; display: flex; align-items: center; justify-content: space-between; padding: 0 8px;
    font-size: 11px; font-style: italic; color: #aaa; }
  .search-box svg { width: 11px; height: 11px; }

  .hero { position: absolute; top: 130px; left: 0; width: 1200px; height: 362px;
    background: linear-gradient(90deg, #f6f6f6, #ffffff 45%, #f2f2f2); }
  .hero-photo { position: absolute; left: 600px; top: 0; width: 430px; height: 362px;
    background: linear-gradient(90deg, rgba(255,255,255,0) 0%, #c9d4de 30%, #5d6f86 70%, #2a3a52 100%); }
  .hero-mark { position: absolute; left: 171px; top: 40px; width: 40px; height: 40px; border-radius: 50%; background: var(--navy); }
  .hero-title { position: absolute; left: 171px; top: 74px; font-size: 34px; font-weight: 700; letter-spacing: -0.5px; }
  .hero-title .accent { color: var(--blue-text); }
  .hero-copy { position: absolute; left: 171px; top: 122px; width: 452px; font-size: 13.5px; line-height: 17px; color: var(--grey-text); }
  .cta-signup { position: absolute; left: 168px; top: 240px; width: 259px; height: 57px; border-radius: 4px;
    background: linear-gradient(#9cc226, var(--green-dark)); color: var(--white); font-size: 24px; font-weight: 600;
    display: flex; align-items: center; justify-content: center; gap: 10px; }
  .cta-signup svg { width: 20px; height: 20px; }
  .call-us { position: absolute; left: 439px; top: 242px; color: var(--green-text); font-size: 22px; font-weight: 700; line-height: 24px; }
  .call-us .phone { display: block; color: var(--navy); font-size: 21px; }
  .slide-arrow { position: absolute; top: 148px; width: 34px; height: 34px; border-radius: 50%; background: #d6d6d6;
    display: flex; align-items: center; justify-content: center; }
  .slide-arrow svg { width: 12px; height: 12px; }
  .slide-arrow.prev { left: 53px; }
  .slide-arrow.next { left: 1104px; }

  .features { position: absolute; top: 492px; left: 0; width: 1200px; height: 379px; background: var(--panel); }
  .feature-card { position: absolute; top: 43px; width: 266px; height: 300px; background: var(--white);
    border: 1px solid var(--card-border); box-shadow: 0 1px 3px rgba(0,0,0,0.12); }
  .feature-card.is-highlighted { background: linear-gradient(#ffffff 40%, #dcf0fb); }
  .feature-media { position: absolute; left: 19px; top: 19px; width: 227px; height: 138px; }
  .feature-title { position: absolute; left: 19px; top: 123px; width: 227px; height: 34px; padding-left: 14px;
    background: rgba(0,0,0,0.35); color: var(--white); font-size: 16px; font-weight: 600; display: flex; align-items: center; }
  .feature-text { position: absolute; left: 19px; top: 171px; width: 227px; font-size: 12.3px; line-height: 15.5px;
    color: var(--grey-text); text-align: justify; }
  .is-highlighted .feature-text { color: var(--blue-text); }
  .read-more { position: absolute; left: 19px; top: 254px; width: 103px; height: 26px; border: 1px solid #cfcfcf;
    border-radius: 2px; background: linear-gradient(#fbfbfb, #e8e8e8); color: #555; font-size: 12px;
    display: flex; align-items: center; justify-content: center; gap: 6px; }
  .is-highlighted .read-more { background: linear-gradient(#1aa0dc, #0b7cbc); border-color: #0b7cbc; color: var(--white); }
  .read-more svg { width: 11px; height: 11px; }

  .site-footer { position: absolute; top: 871px; left: 0; width: 1200px; height: 98px; background: var(--footer); }
  .footer-nav { position: absolute; left: 168px; top: 24px; display: flex; gap: 18px; list-style: none;
    font-size: 12px; color: var(--white); }
  .social-bottom { position: absolute; right: 170px; top: 22px; display: flex; gap: 4px; }
  .footer-rule { position: absolute; left: 0; top: 62px; width: 1200px; height: 1px; background: var(--footer-line); }
  .copyright { position: absolute; left: 168px; top: 76px; font-size: 10px; color: #8a8a8a; }
</style>
</head>
<body>
  <div class="top-strip"></div>

  <header class="site-header">
    <a class="brand" href="#"><span class="brand-dot"></span><span class="brand-name">Prospix</span></a>
    <div class="utility-tabs">
      <a class="utility-tab" href="#"><svg viewBox="0 0 10 10"><circle cx="5" cy="3" r="2.3"/><path d="M0.5 10c0-3 2-4.5 4.5-4.5S9.5 7 9.5 10z"/></svg>Sign In</a>
      <a class="utility-tab" href="#"><svg viewBox="0 0 10 10"><circle cx="5" cy="5" r="5"/></svg>Help</a>
    </div>
    <div class="contact-email">
      <svg width="11" height="8" viewBox="0 0 11 8"><rect x="0.5" y="0.5" width="10" height="7" fill="none" stroke="#aaa"/><path d="M0.5 0.5l5 4 5-4" fill="none" stroke="#aaa"/></svg>
      info@prospix.com
    </div>
    <div class="social-top">
      <a class="social-chip" href="#">chatterlane</a>
      <a class="social-chip" href="#">quipstream</a>
      <a class="social-chip" href="#">orbitly+</a>
      <a class="social-chip" href="#">workNest</a>
    </div>
  </header>

  <nav class="main-nav">
    <ul class="nav-list">
      <li><a href="#">Home</a></li>
      <li><a href="#">About Us</a></li>
      <li><a href="#">Team</a></li>
      <li class="is-active"><a href="#">Customers</a></li>
      <li><a href="#">Jobs</a></li>
      <li><a href="#">Contact Us</a></li>
      <li><a href="#">Sign UP</a></li>
    </ul>
    <div class="search-box">Search here..
      <svg viewBox="0 0 12 12"><circle cx="5" cy="5" r="3.8" fill="none" stroke="#999" stroke-width="1.5"/><path d="M8 8l3 3" stroke="#999" stroke-width="1.5"/></svg>
    </div>
  </nav>

  <section class="hero">
    <div class="hero-photo" role="img" aria-label="Photo of three business professionals in suits standing beside a flip chart"></div>
    <span class="hero-mark"></span>
    <h1 class="hero-title"><span class="accent">Create Surveys.</span> Get Answers.</h1>
    <p class="hero-copy">Lorem Ipsum is simply dummy text of the printing and typesetting industry. Lorem Ipsum has been the industry's standard dummy text ever since the 1500s, when an unknown printer took a galley of type and scrambled it to make a type specimen book.</p>
    <a class="cta-signup" href="#">Sign Up - It's Free!
      <svg viewBox="0 0 20 20"><circle cx="10" cy="10" r="10" fill="#fff"/><path d="M5.5 10.5l3 3 6-6.5" fill="none" stroke="#7fa516" stroke-width="2.6"/></svg>
    </a>
    <div class="call-us">Call Us:<span class="phone">(555) 014-2290</span></div>
    <a class="slide-arrow prev" href="#" aria-label="Previous slide"><svg viewBox="0 0 12 12"><path d="M8 1L3 6l5 5" fill="none" stroke="#fff" stroke-width="2.5"/></svg></a>
    <a class="slide-arrow next" href="#" aria-label="Next slide"><svg viewBox="0 0 12 12"><path d="M4 1l5 5-5 5" fill="none" stroke="#fff" stroke-width="2.5"/></svg></a>
  </section>

  <section class="features">
    <article class="feature-card" style="left:168px">
      <div class="feature-media" role="img" aria-label="Photo of colleagues working together at an office desk" style="background:linear-gradient(135deg,#c8b79a,#8a7560 55%,#3c3a3a)"></div>
      <h2 class="feature-title">Fresh Data</h2>
      <p class="feature-text">Lorem Ipsum is simply dummy text of the printing and typesetting industry. Lorem Ipsum has been the industry's standard dummy text ever since the when an unknown printer took a galley.</p>
      <a class="read-more" href="#">Read More <svg viewBox="0 0 12 12"><circle cx="6" cy="6" r="6" fill="#555"/><path d="M5 3.5L7.5 6 5 8.5" fill="none" stroke="#fff" stroke-width="1.5"/></svg></a>
    </article>
    <article class="feature-card is-highlighted" style="left:468px">
      <div class="feature-media" role="img" aria-label="Photo of a team meeting around a table with laptops" style="background:linear-gradient(135deg,#d8d2c4,#8c8478 50%,#3a3530)"></div>
      <h2 class="feature-title">Sales Intelligence</h2>
      <p class="feature-text">Lorem Ipsum is simply dummy text of the printing and typesetting industry. Lorem Ipsum has been the industry's standard dummy text ever since the when an unknown printer took a galley.</p>
      <a class="read-more" href="#">Read More <svg viewBox="0 0 12 12"><circle cx="6" cy="6" r="6" fill="#fff"/><path d="M5 3.5L7.5 6 5 8.5" fill="none" stroke="#0b7cbc" stroke-width="1.5"/></svg></a>
    </article>
    <article class="feature-card" style="left:766px">
      <div class="feature-media" role="img" aria-label="Illustration of rising blue bar chart with an orange growth arrow" style="background:linear-gradient(160deg,#ffffff,#cfe6f5 55%,#3b8fce)"></div>
      <h2 class="feature-title">Increased Bottomline</h2>
      <p class="feature-text">Lorem Ipsum is simply dummy text of the printing and typesetting industry. Lorem Ipsum has been the industry's standard dummy text ever since the when an unknown printer took a galley.</p>
      <a class="read-more" href="#">Read More <svg viewBox="0 0 12 12"><circle cx="6" cy="6" r="6" fill="#555"/><path d="M5 3.5L7.5 6 5 8.5" fill="none" stroke="#fff" stroke-width="1.5"/></svg></a>
    </article>
  </section>

  <footer class="site-footer">
    <ul class="footer-nav">
      <li><a href="#">Home</a></li>
      <li><a href="#">About Us</a></li>
      <li><a href="#">Team</a></li>
      <li><a href="#">Customers</a></li>
      <li><a href="#">Jobs</a></li>
      <li><a href="#">Contact Us</a></li>
      <li><a href="#">Sign UP</a></li>
    </ul>
    <div class="social-bottom">
      <a class="social-chip" href="#">chatterlane</a>
      <a class="social-chip" href="#">quipstream</a>
      <a class="social-chip" href="#">orbitly+</a>
      <a class="social-chip" href="#">workNest</a>
    </div>
    <div class="footer-rule"></div>
    <p class="copyright">©2013 Prospix Corporation.&nbsp; All Rights Reserved</p>
  </footer>
</body>
</html>
```